BPL its me again- No TIME

I am a weight loss consultant who my target audience now is staff- teachers at work.

I am Bright Path Living and I have partner up with the program Vital Kickoff. I am selling my services but it will be attached to his brochure which I attached to show you.

This flyer will be given to teachers while at work or left on the staff room lunch table.

Please make it short, snappy and fun.
Why lose weight at work? People are time poor

points:-
- Mobile weight loss consultant who comes to you at work
before/after school or lunch break.
-20 minute private 1 on 1 consultations
-limited spots (3 per hour)
-no contract
-10 years experience

If possible I would like it at work flyer for different companies as well like banks but teachers/schools are my main target.

Like the picture with the teacher in front of the board but can remove the heart if possible
Thank you

i will brochure soon to show you

Target Market(s)

people at work- during lunch breaks or before and after
First is school teachers then other companies.
Females are the majority of clients

Industry/Entity Type

Teacher

Requirements
Must have
• leave it up to you just want to grab staff's attention.
Should not have
• please never use the word "diet" its a healthy lifestyle.

```html
<!DOCTYPE html>
<html lang="en">
<head>
<meta charset="utf-8">
<title>Bright Path Living – Why lose weight at work?</title>
<link rel="stylesheet" href="https://fonts.googleapis.com/css2?family=Gochi+Hand&family=Mulish:wght@400;700&display=swap">
<style>
  :root {
    --stage: #e9e6ea;
    --chalkboard: #464848;
    --chalkboard-edge: #3b3d3d;
    --ledge: #d9a06f;
    --lime: #9dc53c;
    --raspberry: #e8345b;
    --white: #ffffff;
    --mint: #cfe8d2;
    --orange: #f39a5d;
    --pale-lime: #d9ea9b;
    --sky: #8fcdf0;
    --pink: #f3a3b7;
    --photo-light: #cfc9c4;
    --photo-dark: #8a7f78;
  }
  * { box-sizing: border-box; margin: 0; padding: 0; }
  html, body { width: 969px; height: 1200px; overflow: hidden; background: var(--stage); }

  .flyer {
    position: absolute; left: 84px; top: 45px;
    width: 800px; height: 1110px; overflow: hidden;
    font-family: "Mulish", Arial, sans-serif;
    box-shadow: 0 6px 20px rgba(0,0,0,.18);
  }
  .chalkboard {
    position: absolute; left: 0; top: 0; width: 800px; height: 690px;
    background: radial-gradient(ellipse at 40% 40%, var(--chalkboard), var(--chalkboard-edge));
  }
  .chalk-ledge {
    position: absolute; left: 0; top: 668px; width: 800px; height: 22px;
    background: var(--ledge);
  }
  .brand {
    position: absolute; left: 84px; top: 110px;
    display: flex; align-items: center; gap: 14px;
    color: var(--white); font-weight: 700;
  }
  .brand-dot { width: 22px; height: 22px; border-radius: 50%; background: var(--white); }
  .brand-name { font-size: 46px; line-height: 1; letter-spacing: 2px; }
  .brand-tagline { font-size: 24px; line-height: 1; margin-top: 6px; }

  .headline {
    position: absolute; left: 84px; top: 284px;
    font-family: "Gochi Hand", cursive; font-weight: 400;
    font-size: 74px; line-height: 58px;
  }
  .headline span { display: block; }
  .headline .why { color: var(--mint); }
  .headline .lose { color: var(--orange); margin-left: 44px; }
  .headline .weight { color: var(--pale-lime); }
  .headline .at-work { color: var(--sky); }
  .subhead {
    position: absolute; left: 114px; top: 558px;
    color: var(--pink); font-size: 21px; letter-spacing: .5px;
  }
  .teacher-photo {
    position: absolute; left: 452px; top: 112px; width: 348px; height: 556px;
    background: linear-gradient(180deg, var(--photo-dark) 0%, var(--photo-light) 70%);
    border-radius: 160px 160px 0 0;
  }

  .benefits-band {
    position: absolute; left: 0; top: 690px; width: 800px; height: 375px;
    background: var(--lime);
  }
  .benefits { list-style: none; position: absolute; left: 81px; top: 40px; color: var(--white); }
  .benefits li {
    position: relative; padding-left: 24px; font-size: 24px; line-height: 34px;
    margin-bottom: 19px;
  }
  .benefits li::before {
    content: ""; position: absolute; left: 0; top: 7px; width: 8px; height: 21px;
    background: var(--white);
  }
  .benefits li.lead { margin-bottom: 24px; }
  .benefits li.lead::before { height: 88px; }
  .benefits strong { font-weight: 700; }
  .partner-badge {
    position: absolute; left: 563px; top: 239px; width: 172px; height: 120px;
    border-radius: 10px; background: var(--white); border: 3px solid var(--raspberry);
    overflow: hidden;
  }
  .partner-badge::after {
    content: ""; position: absolute; left: 0; bottom: 0; width: 100%; height: 26px;
    background: var(--raspberry);
  }
  .footer-band {
    position: absolute; left: 0; top: 1065px; width: 800px; height: 45px;
    background: var(--raspberry);
  }
</style>
</head>
<body>
  <main class="flyer">
    <section class="chalkboard">
      <div class="brand">
        <span class="brand-dot"></span>
        <div>
          <div class="brand-name">BPL</div>
          <div class="brand-tagline">Lifestyle Coach</div>
        </div>
      </div>
      <h1 class="headline">
        <span class="why">Why</span>
        <span class="lose">lose</span>
        <span class="weight">weight</span>
        <span class="at-work">at work?</span>
      </h1>
      <p class="subhead">PEOPLE ARE TIME POOR</p>
      <div class="teacher-photo" role="img" aria-label="Smiling teacher in a striped top holding a green apple in front of a chalkboard"></div>
      <div class="chalk-ledge"></div>
    </section>

    <section class="benefits-band">
      <ul class="benefits">
        <li class="lead">Mobile weight loss consultant<br>who comes to you at work<br>before/after school or lunch break.</li>
        <li>20 minute private 1 on 1 consultations</li>
        <li><strong>LIMITED SPOTS</strong> (3 PER HOUR)</li>
        <li><strong>NO CONTRACT</strong></li>
        <li>10 years experience</li>
      </ul>
      <div class="partner-badge" role="img" aria-label="Vital Kickoff official partner badge"></div>
    </section>

    <div class="footer-band"></div>
  </main>
</body>
</html>
```